Meridian Herbworks Needs a Tri-fold Brochure Design

I need a brochure design that will reflect the freshness of my Los Angeles based company. We cater to high end clientele and stores. I would like the brochure

1. To be consistent in look to my website, product labeling and logo.
2. I want to make sure the information is organized & presented in a clear and easy to follow format. There will need to be a product list in the brochure.
3. Attached you will find the content for the brochure. It is necessary to use the logo. However, it is not necessary to use all of the pictures attached.
4. Please add icons indicating we have accounts on 'Snapfold, Chatterly & Clipboardly"
5. Also my company has a newly registered trademark so in the logo, where it says 'TM' .. this needs to be changed to the encircled 'R' that indicates a registered trademark.
6. I need this to be high quality.
Updates

Hello, Thank you for participating. Please be advised I need a product list that is within some kind of table format. If possible, I want it to be easy to find as this is one of the more important aspects of the brochure. I also don't want my address and phone number to be so large and prominent. I want it neatly tucked away towards the back of the brochure. Also, you don't need to use all of the photos I've attached. Use whatever looks appropriate to your design. However, I do want the photo of the full line in the brochure. I really appreciate elegant and clean designs.

Target Market(s)

high end organic grocery stores, females between the ages of 25-45, people that are into holistic health care

Industry/Entity Type

Health And Wellness

Font styles to use
Serif
Sans Serif

Requirements
Must have
• -My logo
• -all the content I've written on the file that I've uploaded
• -icons indicating that I am on Chatterly, Snapfold and Clipboardly
• -Product list
• -atleast 1 product image, preferably the one of the entire line.
• Please check my website and keep brochure consistent with the feel on the site: thequietmeadowworks.com
Nice to have
• images of product where ever possible
Should not have
• clutter. I don't like sloppy or disorganized marketing materials.

```html
<!DOCTYPE html>
<html lang="en">
<head>
<meta charset="utf-8">
<title>Meridian Herbworks – Tri-fold Brochure</title>
<link href="https://fonts.googleapis.com/css2?family=Open+Sans:wght@300;400;600&display=swap" rel="stylesheet">
<style>
  :root {
    --rose-red: #b23a45;
    --gold: #c9a227;
    --gold-soft: #e4cf7a;
    --cream: #f7f3e4;
    --paper: #f4f2ef;
    --white: #ffffff;
    --ink: #3a3030;
    --grey-text: #8a8585;
    --stage: #e9e7e4;
  }
  * { box-sizing: border-box; margin: 0; padding: 0; }
  html, body { width: 1200px; height: 800px; overflow: hidden; background: var(--stage); }
  body { font-family: "Open Sans", Arial, sans-serif; color: var(--ink); }
  .brochure { position: relative; width: 1200px; height: 800px; background: var(--paper); }
  .brochure-art { position: absolute; inset: 0; }

  .panel { position: absolute; top: 0; width: 400px; height: 800px; }
  .panel--about { left: 0; }
  .panel--contact { left: 400px; }
  .panel--cover { left: 800px; }

  .about-title {
    position: absolute; left: 40px; top: 50px;
    font-size: 34px; font-weight: 400; color: var(--white);
  }
  .about-title span { border-bottom: 2px solid var(--white); }
  .about-body {
    position: absolute; left: 40px; top: 112px; width: 322px;
    font-size: 12.4px; line-height: 1.58; color: var(--white);
    text-align: justify;
  }
  .about-body p { margin-bottom: 12px; text-indent: 16px; }
  .about-body .about-sign { text-align: left; }

  .contact-block { position: absolute; left: 40px; top: 560px; width: 340px; }
  .contact-intro { font-size: 15px; line-height: 1.3; color: var(--ink); margin-bottom: 16px; }
  .contact-list { list-style: none; }
  .contact-item { display: flex; align-items: flex-start; gap: 12px; font-size: 14.5px; line-height: 1.3; margin-bottom: 9px; }
  .contact-icon { flex: 0 0 18px; width: 18px; height: 18px; margin-top: 1px; }

  .cover-title {
    position: absolute; left: 40px; top: 318px; width: 330px;
    font-size: 24px; font-weight: 600; line-height: 1.2; letter-spacing: 0.5px;
    color: var(--white); text-align: center; text-transform: uppercase;
  }
  .brand-mark { position: absolute; right: 40px; top: 640px; display: flex; align-items: center; gap: 12px; }
  .brand-dot { width: 46px; height: 46px; border: 2px solid var(--rose-red); border-radius: 50%; }
  .brand-name { font-size: 22px; font-weight: 300; color: var(--grey-text); }
</style>
</head>
<body>
<main class="brochure">
  <svg class="brochure-art" width="1200" height="800" viewBox="0 0 1200 800" aria-hidden="false">
    <defs>
      <linearGradient id="heroFill" x1="0" y1="0" x2="1" y2="0">
        <stop offset="0" stop-color="#5fa93a"/>
        <stop offset="0.35" stop-color="#9ccf6a"/>
        <stop offset="0.5" stop-color="#e7c58a"/>
        <stop offset="0.75" stop-color="#e8a873"/>
        <stop offset="1" stop-color="#d9c29a"/>
      </linearGradient>
      <linearGradient id="productFill" x1="0" y1="0" x2="1" y2="0">
        <stop offset="0" stop-color="#f3d6da"/>
        <stop offset="0.45" stop-color="#ffffff"/>
        <stop offset="0.6" stop-color="#b5473f"/>
        <stop offset="0.75" stop-color="#ffffff"/>
        <stop offset="0.9" stop-color="#e8738f"/>
        <stop offset="1" stop-color="#ffffff"/>
      </linearGradient>
      <linearGradient id="lowerFill" x1="0" y1="0" x2="0" y2="1">
        <stop offset="0" stop-color="#f1ead0"/>
        <stop offset="1" stop-color="#fbf8ee"/>
      </linearGradient>
      <linearGradient id="titleWave" x1="0" y1="0" x2="1" y2="0">
        <stop offset="0" stop-color="#b58a2a" stop-opacity="0.55"/>
        <stop offset="1" stop-color="#8f6a1e" stop-opacity="0.7"/>
      </linearGradient>
    </defs>

    <!-- about panel -->
    <rect x="0" y="0" width="400" height="800" fill="var(--white)"/>
    <path d="M0 660 C120 610 260 700 400 640 V800 H0 Z" fill="url(#productFill)" role="img" aria-label="Photo of the product bottle beside a bowl of rose petals and a pink rose"/>
    <path d="M0 0 H400 V600 C300 660 150 560 0 650 Z" fill="var(--rose-red)"/>
    <path d="M0 662 C150 575 300 670 400 612" fill="none" stroke="var(--gold)" stroke-width="5"/>

    <!-- contact + cover backgrounds -->
    <rect x="400" y="0" width="800" height="800" fill="var(--paper)"/>
    <path d="M400 440 C560 500 700 430 800 470 C950 520 1100 460 1200 480 V800 H400 Z" fill="url(#lowerFill)" role="img" aria-label="Faded photo of golden dried flower petals"/>
    <path d="M400 250 C520 150 620 110 720 0 H1200 V430 C1060 400 930 460 800 445 C650 430 540 370 400 430 Z" fill="url(#heroFill)" role="img" aria-label="Photo of green blossoms and a young woman with closed eyes in warm sunlight"/>
    <path d="M400 230 C520 130 620 90 700 0" fill="none" stroke="var(--gold)" stroke-width="6"/>
    <path d="M470 40 C560 70 640 40 700 10" fill="none" stroke="var(--gold-soft)" stroke-width="4"/>
    <path d="M800 300 C900 280 1050 320 1200 280 V420 C1060 395 930 455 800 440 Z" fill="url(#titleWave)"/>
    <path d="M400 440 C540 390 650 450 800 460 C940 470 1080 410 1200 430" fill="none" stroke="var(--gold)" stroke-width="6"/>
    <path d="M420 470 C560 430 660 480 800 485" fill="none" stroke="var(--gold-soft)" stroke-width="3"/>
    <path d="M960 560 C1050 530 1130 560 1200 520" fill="none" stroke="var(--gold-soft)" stroke-width="3"/>
    <path d="M400 790 C560 760 700 790 800 775 C950 760 1100 790 1200 770" fill="none" stroke="var(--gold-soft)" stroke-width="4"/>
  </svg>

  <section class="panel panel--about">
    <h2 class="about-title"><span>About</span> Us :</h2>
    <div class="about-body">
      <p>Meridian Herbworks is a handmade professional line of flower essence blends created by Lena Halvorsen, Psychologist and Certified Flower Essence Therapist. Our products naturally support emotional equilibrium by drawing upon ancient wisdom and combining it with modern science. Experience the transformative power of flowers.</p>
      <p>Flower Essence are a botanically based healing system that has existed since ancient times. They heal at the deepest level, addressing the root cause of emotional discomfort. Flower essences naturally and effectively support the reduction of stress, fear, grief, sorrow, worry, shock, hopelessness, trauma, nervousness, self-doubt and any other negative emotion an individual may be experiencing. They are safe and can be used by pets and people of all ages. They are not essential oils and are similar to homeopathy.</p>
      <p class="about-sign">Be the best version of you with flower essences by Meridian Herbworks.</p>
    </div>
  </section>

  <section class="panel panel--contact">
    <div class="contact-block">
      <p class="contact-intro">For complete information<br>on our products,&nbsp; Please visit us :</p>
      <ul class="contact-list">
        <li class="contact-item">
          <svg class="contact-icon" viewBox="0 0 18 18"><circle cx="9" cy="9" r="9" fill="var(--rose-red)"/><path d="M9 4a3 3 0 0 0-3 3c0 2.3 3 6 3 6s3-3.7 3-6a3 3 0 0 0-3-3z" fill="#fff"/><circle cx="9" cy="7" r="1.1" fill="var(--rose-red)"/></svg>
          <span>418 Marigold Ave #12<br>Fernwood Hills, CA 91999</span>
        </li>
        <li class="contact-item">
          <svg class="contact-icon" viewBox="0 0 18 18"><circle cx="9" cy="9" r="9" fill="var(--rose-red)"/><path d="M6 4.5l1.6 2.2-1 1.1c.6 1.3 1.5 2.2 2.7 2.7l1.1-1 2.1 1.6-.8 1.7c-3.5 0-6.6-3.1-6.6-6.6z" fill="#fff"/></svg>
          <span>1-555-014-2290</span>
        </li>
        <li class="contact-item">
          <svg class="contact-icon" viewBox="0 0 18 18"><circle cx="9" cy="9" r="9" fill="var(--rose-red)"/><rect x="4.5" y="6" width="9" height="6.5" fill="#fff"/><path d="M4.5 6l4.5 3.5L13.5 6" fill="none" stroke="var(--rose-red)" stroke-width="1"/></svg>
          <span>info@thequietmeadowworks.com</span>
        </li>
        <li class="contact-item">
          <svg class="contact-icon" viewBox="0 0 18 18"><circle cx="9" cy="9" r="9" fill="var(--rose-red)"/><circle cx="9" cy="9" r="4.5" fill="none" stroke="#fff" stroke-width="1.2"/><path d="M4.5 9h9M9 4.5c-2 2.5-2 6.5 0 9M9 4.5c2 2.5 2 6.5 0 9" fill="none" stroke="#fff" stroke-width="1"/></svg>
          <span>www.thequietmeadowworks.com</span>
        </li>
      </ul>
    </div>
  </section>

  <section class="panel panel--cover">
    <h1 class="cover-title">Meridian Herbworks Be<br>the Best You</h1>
    <div class="brand-mark">
      <span class="brand-dot"></span>
      <span class="brand-name">meridian herbworks</span>
    </div>
  </section>
</main>
</body>
</html>
```